Video Production Company Website

A video production company website for "Quiet Fern Studios"
Home page must have video player and way to select between 3 different videos.

Company does video Post production : Editing, Motion Graphics, Color correction, and Aerial videography

Design should be simple but Pro looking..

Earthy color palette with slight texture..

Industry/Entity Type

Film Production

Number of Pages Required

3 page

Font styles to use
Sans Serif
Other font styles liked:

Requirements
Nice to have
• Thumbnails on homepage to past project clips
Should not have
• full page video

```html
<!DOCTYPE html>
<html lang="en">
<head>
<meta charset="utf-8">
<title>Quiet Fern Studios – Video Production</title>
<link href="https://fonts.googleapis.com/css2?family=Open+Sans:wght@400;600;700&family=Lora:wght@400&display=swap" rel="stylesheet">
<style>
:root{
  --moss:#5e7344;
  --moss-dark:#46582f;
  --bark:#3b2e22;
  --clay:#b5683a;
  --clay-light:#cf8b58;
  --clay-deep:#94522a;
  --sand:#efe6d6;
  --text:#4e463d;
  --muted:#8a8075;
  --line:#e2dccf;
  --bg:#fbf8f2;
  --panel:#f3ede2;
}
*{box-sizing:border-box;margin:0;padding:0}
html,body{width:1200px;height:2312px;overflow:hidden}
body{font-family:"Open Sans",Arial,sans-serif;color:var(--text);background:var(--bg);position:relative;font-size:13px;line-height:1.5}
.abs{position:absolute}
.serif{font-family:"Lora",Georgia,serif}
.texture{background-image:repeating-linear-gradient(45deg,rgba(255,255,255,.04) 0 2px,rgba(0,0,0,.03) 2px 4px)}

/* header */
.brand{left:30px;top:18px;font-size:46px;font-weight:700;color:var(--moss);letter-spacing:-1px;display:flex;align-items:center;gap:10px}
.brand-dot{width:14px;height:14px;background:var(--moss);display:inline-block}
.top-links{right:20px;top:0;background:var(--moss);color:#fff;font-size:12px;padding:3px 16px;border-radius:0 0 4px 4px}
.socials{right:30px;top:74px;display:flex;gap:6px}
.socials span{width:24px;height:24px;border-radius:3px;display:block}
.nav{left:112px;top:122px;width:976px;height:34px;background:var(--moss);display:flex;align-items:center;padding-left:18px;gap:42px}
.nav a{color:#fff;text-decoration:none;font-size:13px;font-weight:600}

/* hero */
.hero{left:0;top:156px;width:1200px;height:340px;background-color:var(--clay)}
.hero-bg{position:absolute;inset:0;background:radial-gradient(ellipse at 65% 45%,var(--clay-light) 0%,var(--clay) 45%,var(--clay-deep) 100%)}
.hero h1{position:absolute;left:210px;top:90px;font-weight:400;font-size:40px;color:#fff}
.hero p{position:absolute;left:210px;top:148px;width:300px;color:#fff;font-size:14px;line-height:1.6}
.player{position:absolute;left:640px;top:26px;width:330px}
.screen{position:relative;height:186px;border-radius:8px 8px 0 0;background:linear-gradient(160deg,#6d6a52 0%,#4a4636 55%,#2c291f 100%);display:flex;align-items:center;justify-content:center}
.controls{height:24px;background:var(--bark);border-radius:0 0 8px 8px;display:flex;align-items:center;gap:10px;padding:0 10px;color:#e9dcc6;font-size:10px}
.bar{flex:1;height:4px;background:rgba(255,255,255,.25);border-radius:2px;position:relative}
.bar i{position:absolute;left:0;top:0;bottom:0;width:35%;background:var(--clay-light);border-radius:2px}
.picks{display:flex;gap:8px;margin-top:10px}
.pick{flex:1;height:52px;border-radius:4px;border:2px solid rgba(255,255,255,.45);position:relative;overflow:hidden}
.pick.on{border-color:#fff}
.pick span{position:absolute;left:0;right:0;bottom:0;background:rgba(59,46,34,.75);color:#fff;font-size:10px;text-align:center;padding:1px 0}
.dots{position:absolute;left:0;right:0;bottom:12px;display:flex;justify-content:center;gap:8px}
.dots i{width:10px;height:10px;border-radius:50%;background:rgba(255,255,255,.55)}
.dots i.on{background:#fff}

/* three columns */
.phases{left:120px;top:560px;width:960px;display:flex;gap:40px}
.phase{flex:1;position:relative;min-height:200px}
.phase h3{font-weight:400;font-size:20px;color:var(--moss);margin-bottom:12px}
.phase .ic{position:absolute;right:0;top:0;width:40px;height:40px}
.phase p{font-size:12px;color:var(--muted);line-height:1.7}
.more{display:inline-block;font-size:11px;color:var(--text);margin-top:10px;float:right}
.more:after{content:"";display:inline-block;width:14px;height:14px;border-radius:50%;background:var(--moss);margin-left:6px;vertical-align:middle}

.section-label{left:120px;font-size:12px;text-transform:uppercase;color:var(--muted);letter-spacing:.5px}
.rule{left:120px;width:960px;height:1px;background:var(--line)}

/* recent work */
.work{left:120px;top:826px;width:960px;display:flex;gap:20px}
.work div{flex:1;height:112px;border:1px solid var(--line)}

/* clients */
.clients{left:120px;top:990px;width:960px;display:flex;gap:12px}
.client{flex:1;height:70px;display:flex;align-items:center;justify-content:center;font-weight:700;font-size:16px;border:1px solid var(--line);color:#fff}

/* blog */
.blog{left:120px;top:1126px;width:960px;display:flex;gap:40px}
.post{flex:1;position:relative;min-height:270px}
.post h4{font-weight:400;font-size:17px;color:var(--text);line-height:1.35;margin-bottom:8px}
.post .date{font-size:10px;color:var(--muted);margin-bottom:8px}
.post p{font-size:11px;color:var(--muted);line-height:1.6;margin-bottom:10px}
.post .thumb{width:100%;height:110px;margin:6px 0 10px}
.btn{position:absolute;right:0;bottom:0;font-size:11px;color:#fff;background:var(--moss);padding:3px 12px;border-radius:3px}

.older{left:120px;top:1506px;font-size:11px;color:var(--text)}

/* services & testimonial */
.services{left:120px;top:1548px;width:500px;border:1px solid var(--line);background:#fff}
.services h5,.testi h5{font-size:12px;font-weight:400;text-transform:uppercase;color:var(--muted);padding:10px 16px;border-bottom:1px solid var(--line)}
.services ul{list-style:none}
.services li{display:flex;align-items:center;gap:12px;padding:13px 16px;border-bottom:1px solid var(--line);font-size:13px}
.services li:last-child{border-bottom:0}
.services li svg{flex:none}
.testi{left:660px;top:1548px;width:420px;border:1px solid var(--line);background:#fff}
.quote{margin:18px;background:var(--panel);padding:18px 20px;font-size:11px;line-height:1.6;color:var(--muted);position:relative}
.quote:after{content:"";position:absolute;left:30px;bottom:-10px;border:10px solid transparent;border-top-color:var(--panel);border-bottom:0}
.author{display:flex;align-items:center;gap:10px;margin:18px;font-size:11px}
.author .av{width:40px;height:40px;background:#c9b9a6}

/* process band */
.process{left:0;top:2040px;width:1200px;height:124px;background-color:var(--clay)}
.process-bg{position:absolute;inset:0;background:linear-gradient(90deg,var(--clay-deep),var(--clay),var(--clay-deep))}
.process h2{position:absolute;left:120px;top:28px;font-weight:400;color:#fff;font-size:24px;line-height:1.2;width:170px}
.steps{position:absolute;left:320px;top:22px;display:flex;align-items:flex-start;gap:14px}
.step{width:150px;text-align:center;color:#fff;font-size:11px}
.step .sic{width:46px;height:46px;border-radius:50%;border:2px solid #fff;margin:0 auto 8px;background:rgba(255,255,255,.2)}
.arrow{margin-top:14px}

.cta{left:0;width:1200px;top:2172px;text-align:center;font-size:15px;color:var(--text)}
.cta b{color:var(--clay);font-weight:600}

/* footer */
.footer{left:0;top:2204px;width:1200px;height:108px;background-color:var(--bark)}
.footer .fbrand{position:absolute;left:30px;top:20px;font-size:40px;font-weight:700;color:#fff;display:flex;align-items:center;gap:8px}
.footer .fbrand span{width:12px;height:12px;background:#fff;display:inline-block}
.footer .copy{position:absolute;left:30px;top:80px;font-size:11px;color:#d6c8b3}
.news{position:absolute;left:700px;top:16px;color:#fff}
.news h6{font-size:18px;font-weight:400;margin-bottom:8px}
.news .field{width:320px;height:24px;background:#fff;border-radius:2px;font-size:11px;color:#999;padding:4px 8px}
.news .go{position:absolute;left:330px;top:38px;width:56px;height:24px;background:var(--clay);border-radius:2px;color:#fff;font-size:11px;text-align:center;line-height:24px}
</style>
</head>
<body>

<header>
  <div class="abs brand">quietfern.<span class="brand-dot"></span></div>
  <div class="abs top-links">Login | Contact us</div>
  <div class="abs socials">
    <span style="background:#a45a3c"></span><span style="background:#5e6b4a"></span><span style="background:#b5683a"></span><span style="background:#8a9a6c"></span><span style="background:#6e5a44"></span><span style="background:#8c4a32"></span>
  </div>
  <nav class="abs nav">
    <a>Home</a><a>About Quiet Fern</a><a>Services</a><a>Clients</a><a>Portfolio</a><a>Careers</a><a>Contact us</a><a>Blog</a>
  </nav>
</header>

<section class="abs hero">
  <div class="hero-bg"></div>
  <div class="hero-bg texture"></div>
  <h1 class="serif">Multimedia Services</h1>
  <p><strong>Quiet Fern</strong> is a pioneer in designing Multimedia Presentations and Demos for the last decade.</p>
  <div class="player">
    <div class="screen" role="img" aria-label="Featured showreel video frame">
      <svg width="56" height="56" viewBox="0 0 56 56"><circle cx="28" cy="28" r="26" fill="rgba(255,255,255,.85)"/><path d="M22 17l18 11-18 11z" fill="#3b2e22"/></svg>
    </div>
    <div class="controls"><span>0:42</span><div class="bar"><i></i></div><span>2:10</span></div>
    <div class="picks">
      <div class="pick on" role="img" aria-label="Editing reel thumbnail" style="background:linear-gradient(135deg,#8a7b5c,#4d4433)"><span>Editing</span></div>
      <div class="pick" role="img" aria-label="Motion graphics reel thumbnail" style="background:linear-gradient(135deg,#9aa57c,#5e7344)"><span>Motion Graphics</span></div>
      <div class="pick" role="img" aria-label="Aerial reel thumbnail" style="background:linear-gradient(135deg,#c9b79a,#7d6a4d)"><span>Aerial</span></div>
    </div>
  </div>
  <div class="dots"><i class="on"></i><i></i><i></i></div>
</section>

<section class="abs phases">
  <div class="phase">
    <svg class="ic" viewBox="0 0 40 40"><circle cx="20" cy="20" r="18" fill="none" stroke="#5e7344" stroke-width="2"/><path d="M13 14h14M13 20h14M13 26h9" stroke="#5e7344" stroke-width="2"/></svg>
    <h3 class="serif">Pre Production</h3>
    <p>Our ideas will fire first, hearts and business goals in the market. We start it all off with a clear plan, script and sketches that guide every shoot, making the whole journey easy and smooth from start to finish.</p>
    <span class="more">Learn More</span>
  </div>
  <div class="phase">
    <svg class="ic" viewBox="0 0 40 40"><rect x="4" y="12" width="22" height="18" rx="2" fill="none" stroke="#5e7344" stroke-width="2"/><path d="M26 18l10-5v16l-10-5z" fill="#5e7344"/></svg>
    <h3 class="serif">Production</h3>
    <p>Quiet Fern Studios is a leading video production company. A full crew covers every shoot with gear that fits the brief, from small studio sets to large outdoor scenes and aerial work.</p>
    <span class="more">Learn More</span>
  </div>
  <div class="phase">
    <svg class="ic" viewBox="0 0 40 40"><rect x="4" y="8" width="32" height="22" rx="2" fill="none" stroke="#5e7344" stroke-width="2"/><path d="M14 34h12M20 30v4" stroke="#5e7344" stroke-width="2"/></svg>
    <h3 class="serif">Post Production</h3>
    <p>Quiet Fern Studios is one of the top post production houses around. We handle editing, motion graphics, colour correction, sound mixing and final delivery under one roof.</p>
    <span class="more">Learn More</span>
  </div>
</section>

<div class="abs section-label" style="top:792px">Recent Work</div>
<div class="abs rule" style="top:812px"></div>
<section class="abs work">
  <div role="img" aria-label="Project thumbnail: explainer video still" style="background:linear-gradient(135deg,#ece5d6,#cdbf9f)"></div>
  <div role="img" aria-label="Project thumbnail: animated product clip" style="background:linear-gradient(135deg,#e3e8d6,#9fae80)"></div>
  <div role="img" aria-label="Project thumbnail: corporate film frame" style="background:linear-gradient(135deg,#f2e4d2,#c98a5a)"></div>
  <div role="img" aria-label="Project thumbnail: documentary scene" style="background:linear-gradient(135deg,#ebe6de,#b2a898)"></div>
</section>

<div class="abs section-label" style="top:956px">Our Clients</div>
<div class="abs rule" style="top:976px"></div>
<section class="abs clients">
  <div class="client" style="background:#6e665a">Hazelbrook</div>
  <div class="client" style="background:#5e7344">Blue Harbor</div>
  <div class="client" style="background:#fff;color:#5e7344">Tarn Group</div>
  <div class="client" style="background:#fff;color:#3b2e22">Twinmill</div>
  <div class="client" style="background:#fff;color:#a24f2a">Sunfield Staffing</div>
</section>

<div class="abs section-label" style="top:1092px">From Our Blog</div>
<div class="abs rule" style="top:1112px"></div>
<section class="abs blog">
  <article class="post">
    <h4 class="serif">Why You Need an Animated Video for Your Product?</h4>
    <div class="date">September 24, 2015</div>
    <p>Animated videos help buyers grasp what your product does in seconds. A short clip can explain a tricky idea, hold attention and lift sales.</p>
    <p>What an animated video can add for your product page and how to plan a script that works.</p>
    <span class="btn">Read More</span>
  </article>
  <article class="post">
    <h4 class="serif">Why You Need A Video For Your Educational Institute?</h4>
    <div class="date">August 18, 2015</div>
    <p>Schools and colleges use video to show campus life, share lessons and reach new students in a way brochures can not.</p>
    <p>Video helps parents and students see what you offer and why it matters before they ever visit.</p>
    <span class="btn">Read More</span>
  </article>
  <article class="post">
    <h4 class="serif">Video Editing Company in Mumbai</h4>
    <div class="date">February 12, 2015</div>
    <div class="thumb" role="img" aria-label="Photo of an editor at a video editing workstation" style="background:linear-gradient(135deg,#3a2c22,#c7a16a)"></div>
    <p>By providing the best post production services, Quiet Fern Studios has become a trusted video editing partner.</p>
    <span class="btn">Read More</span>
  </article>
</section>

<div class="abs rule" style="top:1490px"></div>
<div class="abs older">&laquo; Older Posts</div>

<section class="abs services">
  <h5>Our Services</h5>
  <ul>
    <li><svg width="18" height="18" viewBox="0 0 18 18"><circle cx="9" cy="9" r="8" fill="#b5683a"/><path d="M7 5l4 4-4 4" stroke="#fff" stroke-width="2" fill="none"/></svg>Explainer Video Production</li>
    <li><svg width="18" height="18" viewBox="0 0 18 18"><circle cx="9" cy="9" r="8" fill="#b5683a"/><path d="M7 5l4 4-4 4" stroke="#fff" stroke-width="2" fill="none"/></svg>Web Video Production</li>
    <li><svg width="18" height="18" viewBox="0 0 18 18"><circle cx="9" cy="9" r="8" fill="#b5683a"/><path d="M7 5l4 4-4 4" stroke="#fff" stroke-width="2" fill="none"/></svg>TV Commercial Production</li>
    <li><svg width="18" height="18" viewBox="0 0 18 18"><circle cx="9" cy="9" r="8" fill="#b5683a"/><path d="M7 5l4 4-4 4" stroke="#fff" stroke-width="2" fill="none"/></svg>Corporate Film Production</li>
    <li><svg width="18" height="18" viewBox="0 0 18 18"><circle cx="9" cy="9" r="8" fill="#b5683a"/><path d="M7 5l4 4-4 4" stroke="#fff" stroke-width="2" fill="none"/></svg>Documentary Film Production</li>
    <li><svg width="18" height="18" viewBox="0 0 18 18"><circle cx="9" cy="9" r="8" fill="#b5683a"/><path d="M7 5l4 4-4 4" stroke="#fff" stroke-width="2" fill="none"/></svg>Music Video Production</li>
    <li><svg width="18" height="18" viewBox="0 0 18 18"><circle cx="9" cy="9" r="8" fill="#b5683a"/><path d="M7 5l4 4-4 4" stroke="#fff" stroke-width="2" fill="none"/></svg>Promotional Video Production</li>
    <li><svg width="18" height="18" viewBox="0 0 18 18"><circle cx="9" cy="9" r="8" fill="#b5683a"/><path d="M7 5l4 4-4 4" stroke="#fff" stroke-width="2" fill="none"/></svg>Educational Video Production</li>
  </ul>
</section>

<section class="abs testi">
  <h5>Testimonials</h5>
  <div class="quote">I was in need of an explainer video which would clearly tell buyers what we sell and why it matters. Quiet Fern understood the brief, kept us informed at each step and delivered on time. We have used their team again for product demos and training clips, and the quality has stayed just as high.</div>
  <div class="author"><div class="av" role="img" aria-label="Client portrait"></div><span><b>Jean Marlow</b> , Tidewater Foods Ltd.</span></div>
</section>

<section class="abs process">
  <div class="process-bg"></div>
  <div class="process-bg texture"></div>
  <h2 class="serif">Corporate Films Process</h2>
  <div class="steps">
    <div class="step"><div class="sic"></div>Concept Script Development</div>
    <svg class="arrow" width="40" height="16" viewBox="0 0 40 16"><path d="M0 8h32M26 2l8 6-8 6" stroke="#fff" stroke-width="2" fill="none"/></svg>
    <div class="step"><div class="sic"></div>Shooting &amp; photography</div>
    <svg class="arrow" width="40" height="16" viewBox="0 0 40 16"><path d="M0 8h32M26 2l8 6-8 6" stroke="#fff" stroke-width="2" fill="none"/></svg>
    <div class="step"><div class="sic"></div>Editing &amp; Special Effects</div>
    <svg class="arrow" width="40" height="16" viewBox="0 0 40 16"><path d="M0 8h32M26 2l8 6-8 6" stroke="#fff" stroke-width="2" fill="none"/></svg>
    <div class="step"><div class="sic"></div>Dubbing &amp; Delivery</div>
  </div>
</section>

<p class="abs cta">Have seen our corporate video production services? Please <b>contact us now!</b></p>

<footer class="abs footer texture">
  <div class="fbrand">quietfern.<span></span></div>
  <div class="copy">copyright 2015 @ Quiet Fern Studios</div>
  <div class="news">
    <h6>Sign up for our newsletter</h6>
    <div class="field">Please enter your e-mail id</div>
    <div class="go">Submit</div>
  </div>
</footer>

</body>
</html>
```